LunaGowns.com Banner AD

We are looking for some talented creators to create for us a banner ad for our online clothing store that specializes in dresses. We are looking for a fresh, clean, and sleek KORA, P&Q, and Glint appeal- clean, modern and sophisticated.

We would like for the final project to appear professionally done, we've had projects completed by several talent out there that did not capture our image, and let's just say it was too cluttered and appeared as if a high school editor had completed it.

I have attached a few files for you to reference, I have File 1, 2, 3, 8 and the P&Q photos as examples of what we DO like.

I have attached File 5, which is the work of one the designers that was working on this project. Although it is very simple and gets the point across, it doesn't come across like a magazine editorial.

I have attached File 6, that is the main photo we wish to use for our banner.

I have attached File 7, which is what a creator had done for us via Brevora.com, that is a good example of what we do NOT want.

That is about sums it up! I hope the examples are useful tools for you!

Hi Designers!

Thank you so much for your submissions! I enjoy viewing each and every one of them! Please view my update on what I am looking for, I have made some adjustments and have added a few more examples to reference, I have made my direction a bit more clearer. Because it seems some designers are not quite understanding my direction. I know you all have amazing talent and I am hoping to see something I am looking for and I love soon! If you have any other questions, please don't hesitate to ask! 

Target Market(s)

Our company targets women of all ages, we carry dresses that cater to every occasion, whether its an older woman looking for a dress to attend a wedding or a teenager looking for a prom dress. We want our front page banner to appear fresh, clean, with a feminine touch, we want to stray from tacky (gradients, etc..) and keep it classy all while maintaining that magazine editorial element, we want to be more fashion focused, like Glint. We want this project to appear professionally done. Our desired concept is something out of a magazine editorial, not too much going on, while shifting focus more on the dress itself than a design element like flowers or spring backgrounds.

Industry/Entity Type

High School

Requirements
Must have
• We want a glint fashion appeal, magazine editorial type of look. The phrases below should be included"

"New Season New Sexy Dresses"

"Free U.S shipping on orders $75+"
"Shop our sales up to 60% off"

All of the other phrases do not need to be included. Also, Do not include the parenthesis.
Should not have
• Only include the photo I've attached that appears solo. Please do not include the other 3 dresses that is displayed in a banner that was created for us by another designer. (that is provided as an example only)

```html
<!DOCTYPE html>
<html lang="en">
<head>
<meta charset="utf-8">
<title>LunaGowns.com – New Season Banner</title>
<link rel="stylesheet" href="https://fonts.googleapis.com/css2?family=Josefin+Sans:wght@300;400&display=swap">
<style>
  :root {
    --ink: #1f1f1f;
    --rule: #3a3a3a;
    --pink: #d6278a;
    --pink-deep: #c2136f;
    --button: #cf1d7f;
    --button-dark: #b3126a;
    --paper: #ffffff;
    --photo-pink: #f06aa8;
    --photo-blue: #5a4fb0;
    --photo-skin: #d9a882;
  }
  * { margin: 0; padding: 0; box-sizing: border-box; }
  html, body { width: 1200px; height: 1043px; overflow: hidden; background: var(--paper); }
  .banner {
    position: relative;
    width: 1200px;
    height: 1043px;
    background: var(--paper);
    font-family: "Josefin Sans", "Helvetica Neue", Arial, sans-serif;
    color: var(--ink);
  }
  .model-photo {
    position: absolute;
    left: 110px;
    top: 0;
    width: 540px;
    height: 1043px;
    background:
      linear-gradient(180deg, var(--photo-skin) 0%, var(--photo-skin) 24%, transparent 34%),
      linear-gradient(160deg, var(--photo-pink) 20%, var(--photo-blue) 55%, var(--photo-pink) 85%);
    border-radius: 46% 46% 12% 12% / 18% 18% 4% 4%;
    opacity: 0.85;
  }
  .offer {
    position: absolute;
    left: 610px;
    top: 150px;
    width: 560px;
    text-align: center;
  }
  .headline {
    font-weight: 300;
    font-size: 82px;
    line-height: 1;
    letter-spacing: 1px;
    color: var(--ink);
  }
  .rule {
    display: block;
    height: 2px;
    background: var(--rule);
    margin: 0 auto;
  }
  .rule--wide { width: 540px; margin-top: 22px; }
  .rule--short { width: 246px; }
  .subhead {
    font-weight: 400;
    font-size: 54px;
    line-height: 1;
    color: var(--pink);
    margin-top: 22px;
  }
  .shipping {
    margin-top: 96px;
  }
  .shipping-text {
    font-weight: 400;
    font-size: 40px;
    line-height: 1.15;
    color: var(--ink);
    margin: 30px 0 28px;
    display: inline-block;
    text-align: left;
  }
  .shipping-text small { font-size: 31px; }
  .sale {
    font-weight: 400;
    font-size: 56px;
    color: var(--pink);
    margin-top: 66px;
  }
  .sale strong { font-weight: 400; color: var(--pink-deep); }
  .shop-button {
    display: block;
    width: 452px;
    height: 90px;
    margin: 30px auto 0;
    border-radius: 16px;
    background: linear-gradient(180deg, var(--button) 0%, var(--button-dark) 100%);
    box-shadow: 0 4px 8px rgba(0,0,0,0.25);
    color: var(--paper);
    font-weight: 400;
    font-size: 58px;
    line-height: 96px;
    text-decoration: none;
  }
  .brand {
    margin-top: 66px;
    font-weight: 400;
    font-size: 48px;
    color: var(--ink);
    letter-spacing: 1px;
  }
</style>
</head>
<body>
<main class="banner">
  <div class="model-photo" role="img" aria-label="Smiling woman with long wavy hair posing with hands on hips in a fitted sleeveless pink and blue watercolour-print dress"></div>

  <section class="offer">
    <h1 class="headline">New Season</h1>
    <span class="rule rule--wide"></span>
    <h2 class="subhead">New Sexy Dresses</h2>

    <div class="shipping">
      <span class="rule rule--short"></span>
      <p class="shipping-text">Free U.S shipping<br>on orders <small>$75+</small></p>
      <span class="rule rule--short"></span>
    </div>

    <p class="sale">up to <strong>60%</strong> off</p>
    <a class="shop-button" href="#">shop now &gt;&gt;</a>

    <p class="brand">LunaGowns.com</p>
  </section>
</main>
</body>
</html>
```